Require modern interface design for our website.

We are looking for a redesign of our website interface. The interface and the look and feel needs to be modern and seamless. Designer must be able to integrate with the backend PHP and Java. Please try utilise logo and colours where possible don't go too drastic. We utilise this site for learning and training purposes so please keep in line with that objective.

Target Market(s)

Education

Industry/Entity Type

Education

Number of Pages Required

5+ page

Font styles to use
Sans Serif

Requirements
Must have
• Innovative and modern look, logo to be incorporated.
Nice to have
• Good use of colours
Should not have
• Lack of creativity

```html
<!DOCTYPE html>
<html lang="en">
<head>
<meta charset="utf-8">
<title>Brightwell – Learning</title>
<link href="https://fonts.googleapis.com/css2?family=Open+Sans:ital,wght@0,400;0,600;0,700;1,700&display=swap" rel="stylesheet">
<style>
:root{
  --green:#4cb748;
  --green-dark:#3e9e3b;
  --ink:#3a3a3a;
  --muted:#8a8a8a;
  --line:#e4e4e4;
  --bg-soft:#f4f5f4;
  --navy:#262c36;
  --navy-deep:#1e232b;
  --white:#ffffff;
}
*{margin:0;padding:0;box-sizing:border-box}
html,body{width:674px;height:1200px;overflow:hidden}
body{font-family:"Open Sans",Arial,sans-serif;color:var(--ink);background:var(--white);font-size:10px}
.site-header{height:34px;display:flex;align-items:center;justify-content:space-between;padding:0 40px 0 48px;background:var(--white)}
.brand{font-size:17px;font-weight:700;color:var(--green)}
.main-nav{display:flex;align-items:center;gap:15px;font-size:8px;color:var(--ink)}
.btn-login{background:var(--green);color:var(--white);padding:4px 9px;font-weight:600}
.socials{display:flex;gap:6px}
.socials span{width:8px;height:8px;border-radius:50%;background:var(--green);display:block}
.hero{height:281px;background:
  radial-gradient(ellipse 120px 150px at 560px 150px,#e9c6a8 0%,rgba(233,198,168,0) 100%),
  radial-gradient(ellipse 90px 120px at 560px 40px,#5a3a28 0%,rgba(90,58,40,0) 100%),
  radial-gradient(ellipse 130px 90px at 80px 230px,#3f6fa8 0%,rgba(63,111,168,0) 100%),
  radial-gradient(ellipse 110px 80px at 300px 200px,#b9b4b0 0%,rgba(185,180,176,0) 100%),
  radial-gradient(ellipse 80px 70px at 230px 70px,#c8969a 0%,rgba(200,150,154,0) 100%),
  linear-gradient(100deg,#d9dfe4 0%,#cbbfb6 45%,#e2cfc0 72%,#7e6352 100%)}
.features{height:145px;background:var(--green);display:flex;align-items:center;padding:0 40px 0 90px;gap:28px;color:var(--white)}
.feature{width:140px;text-align:center}
.feature .ico{width:30px;height:30px;margin:0 auto 8px;border-radius:50%;background:var(--green-dark);display:flex;align-items:center;justify-content:center}
.feature h3{font-size:9px;font-weight:700;margin-bottom:5px}
.feature p{font-size:6px;line-height:1.5;opacity:.85}
.features .illus{margin-left:auto;width:150px;height:120px;background:linear-gradient(160deg,#e9f4e8,#c8e4c6);border-radius:4px}
.courses{height:338px;background:var(--bg-soft);padding:22px 64px 0}
.courses-head{display:flex;justify-content:space-between;align-items:flex-end;border-bottom:1px solid var(--line);padding-bottom:8px;margin-bottom:16px}
.courses-head h2{font-size:13px;font-weight:700}
.courses-head p{font-size:6px;color:var(--muted);margin-top:3px}
.view-all{font-size:7px;color:var(--muted);border:1px solid var(--line);padding:3px 6px}
.course-grid{display:flex;gap:12px}
.card{width:128px;background:var(--white);border:1px solid var(--line)}
.card .thumb{height:120px}
.card .body{padding:8px 8px 6px}
.card h4{font-size:7.5px;font-weight:700}
.card .teacher{font-size:6px;color:var(--muted);margin-top:3px}
.card .price{font-size:11px;color:var(--green);font-weight:700;margin:10px 0 6px}
.card .meta{display:flex;justify-content:space-between;border-top:1px solid var(--line);padding-top:5px;font-size:6px;color:var(--muted)}
.stars{color:#f0b429;letter-spacing:1px}
.dots{text-align:center;margin-top:14px}
.dots span{display:inline-block;width:4px;height:4px;border-radius:50%;background:#bbb}
.instructor{height:119px;background:var(--green);display:flex;align-items:center;padding:0 74px 0 76px;color:var(--white)}
.instructor .people{width:160px;height:119px;background:linear-gradient(180deg,#8fc98b,#3f8d3b)}
.instructor .pitch{margin-left:24px;display:flex;align-items:center;gap:10px}
.instructor h3{font-size:15px;font-style:italic;font-weight:700}
.instructor p{font-size:5.5px;opacity:.85;margin-top:3px}
.btn-start{margin-left:auto;border:1px solid var(--white);padding:5px 8px;font-size:7px;font-weight:600}
.contact{height:263px;background:var(--navy);color:var(--white);text-align:center;padding-top:28px}
.contact h2{font-size:14px;font-weight:400;margin-bottom:16px}
.tabs{display:flex;justify-content:center;font-size:8px}
.tabs span{width:110px;padding-bottom:5px;border-bottom:1px solid #444b56}
.tabs .active{color:var(--green);border-bottom:2px solid var(--green)}
.info{display:flex;justify-content:space-around;padding:56px 60px 0}
.info div{width:170px}
.info .circle{width:44px;height:44px;border-radius:50%;background:var(--green);margin:0 auto 12px;display:flex;align-items:center;justify-content:center}
.info h4{font-size:10px;font-weight:600;margin-bottom:3px}
.info p{font-size:6px;opacity:.8}
.site-footer{height:20px;background:var(--navy-deep);color:#9aa;font-size:6px;text-align:center;line-height:20px}
</style>
</head>
<body>
<header class="site-header">
  <div class="brand">Brightwell</div>
  <nav class="main-nav">
    <span>Home</span><span>About</span><span>Courses</span><span>Blog</span><span>Contact</span>
    <span class="btn-login">Login</span>
    <div class="socials"><span></span><span></span><span></span><span></span></div>
  </nav>
</header>

<section class="hero" role="img" aria-label="Smiling teacher in the foreground with a blurred classroom of students behind her"></section>

<section class="features">
  <div class="feature">
    <div class="ico"><svg width="16" height="16" viewBox="0 0 16 16" fill="#fff"><path d="M4 1h8v5a4 4 0 0 1-8 0z"/><rect x="7" y="10" width="2" height="3"/><rect x="4" y="13" width="8" height="2"/></svg></div>
    <h3>Best Industry Leaders</h3>
    <p>Learn from experienced mentors who guide every step of your course and help you grow your skills with care.</p>
  </div>
  <div class="feature">
    <div class="ico"><svg width="16" height="16" viewBox="0 0 16 16" fill="none" stroke="#fff" stroke-width="1.5"><rect x="1.5" y="2" width="13" height="9"/><path d="M5 14h6M8 11v3"/></svg></div>
    <h3>Learn Anything Online</h3>
    <p>Study at your own pace from any device with flexible lessons, clear goals and support whenever you need it.</p>
  </div>
  <div class="illus" role="img" aria-label="Illustration of an open book with a lamp, globe and study items"></div>
</section>

<section class="courses">
  <div class="courses-head">
    <div>
      <h2>Latest Courses</h2>
      <p>Fresh lessons to help you build practical skills and reach your learning goals sooner.</p>
    </div>
    <span class="view-all">View All Courses</span>
  </div>
  <div class="course-grid">
    <article class="card">
      <div class="thumb" role="img" aria-label="Teacher presenting at a whiteboard" style="background:linear-gradient(160deg,#cfe3f0,#7fa9c4)"></div>
      <div class="body"><h4>Living Skills</h4><p class="teacher">Teacher: Dana Wells</p><p class="price">$ 199.00</p>
      <div class="meta"><span>24 students</span><span class="stars">★★★★★</span></div></div>
    </article>
    <article class="card">
      <div class="thumb" role="img" aria-label="Student working on a laptop in a library" style="background:linear-gradient(160deg,#e8dccb,#a88e6f)"></div>
      <div class="body"><h4>Email Basics</h4><p class="teacher">Teacher: Dana Wells</p><p class="price">$ 49.00</p>
      <div class="meta"><span>18 students</span><span class="stars">★★★★★</span></div></div>
    </article>
    <article class="card">
      <div class="thumb" role="img" aria-label="Student writing notes at a desk" style="background:linear-gradient(160deg,#f1e4dc,#b77a5c)"></div>
      <div class="body"><h4>Easy 3D Presentation</h4><p class="teacher">Teacher: Dana Wells</p><p class="price">$ 77.00</p>
      <div class="meta"><span>31 students</span><span class="stars">★★★★★</span></div></div>
    </article>
    <article class="card">
      <div class="thumb" role="img" aria-label="Smiling man in a shirt and glasses" style="background:linear-gradient(160deg,#dfe6ea,#8d9ba4)"></div>
      <div class="body"><h4>Learning Start</h4><p class="teacher">Teacher: Dana Wells</p><p class="price">$ 119.00</p>
      <div class="meta"><span>12 students</span><span class="stars">★★★★★</span></div></div>
    </article>
  </div>
  <div class="dots"><span></span></div>
</section>

<section class="instructor">
  <div class="people" role="img" aria-label="Group of smiling students holding books"></div>
  <div class="pitch">
    <svg width="26" height="20" viewBox="0 0 26 20" fill="none" stroke="#fff" stroke-width="1.6"><path d="M13 4C9 1 4 1 1 2v15c3-1 8-1 12 2 4-3 9-3 12-2V2c-3-1-8-1-12 2zM13 4v15"/></svg>
    <div><h3>Become an Instructor?</h3><p>Share your knowledge and teach learners around the world.</p></div>
  </div>
  <span class="btn-start">Get Started Now!</span>
</section>

<section class="contact">
  <h2>Get In Touch</h2>
  <div class="tabs"><span class="active">Contact Info</span><span>Services Inquiry</span><span>View on Map</span></div>
  <div class="info">
    <div><div class="circle"><svg width="18" height="22" viewBox="0 0 18 22" fill="#fff"><path d="M9 0a8 8 0 0 0-8 8c0 6 8 14 8 14s8-8 8-14a8 8 0 0 0-8-8zm0 11a3 3 0 1 1 0-6 3 3 0 0 1 0 6z"/></svg></div><h4>ADDRESS</h4><p>12 Maple Row, Fairview, 40210</p></div>
    <div><div class="circle"><svg width="20" height="20" viewBox="0 0 20 20" fill="#fff"><path d="M4 1l4 4-2 3c1 2 4 5 6 6l3-2 4 4-3 3C9 19 1 11 1 4z"/></svg></div><h4>PHONES</h4><p>+1 (555) 014-2290, +1 (555) 014-2291</p></div>
    <div><div class="circle"><svg width="22" height="16" viewBox="0 0 22 16" fill="none" stroke="#fff" stroke-width="1.8"><rect x="1" y="1" width="20" height="14"/><path d="M1 1l10 8 10-8"/></svg></div><h4>E-MAIL</h4><p>hello@brightwell.edu, help@brightwell.edu</p></div>
  </div>
</section>

<footer class="site-footer">Copyright © 2024 Brightwell.com All Rights Reserved</footer>
</body>
</html>
```